Postcard, Logo, and Website Design for Direct to Consumer Personal Bankruptcy Service

We are launching a bankruptcy legal practice. Our postcard design will be mailed to prospective clients who have already been sued by their credit card companies.

We would like people to glean from the post card that they can call to set up a no-fee consultation, or to phone our offices, where our receptionist can aid them in setting up a no-fee consultation.

Logo should be professional, but not overly stuffy.

Website copy can be added later, but most important is a space where people can fill out there info so we can reach out to them.

Pertinent info that should be on postcard

Name: Harbor Pines Debt Relief
Phone: 616-392-7158
Website: HPDebtRelief.example

Rough ideas that we've tossed around include the following (but use your own judgement - we're counting on you for creativity):

Creditors Calling?
Mountain of Debt?
Getting Sued?

We can help!

Target Market(s)

People who are thinking about bankruptcy and have already been sued

Industry/Entity Type

Financial Service

Logo Text

Harbor Pines Debt Relief

Number of Pages Required

1 page

Font styles to use
Sans Serif

Colors

Designer to choose colors to be used in the design.

Requirements
Must have
• Space for info about bankruptcy process
• Space for user to submit info

```html
<!DOCTYPE html>
<html lang="en">
<head>
<meta charset="utf-8">
<title>Harbor Pines Debt Relief – Postcard</title>
<link rel="stylesheet" href="https://fonts.googleapis.com/css2?family=Oswald:wght@400;500;600&family=Roboto+Condensed:wght@400&display=swap">
<style>
  :root {
    --page: #ececec;
    --card: #ffffff;
    --navy: #37338f;
    --red: #e8432b;
    --grey: #77787b;
    --ink: #141414;
    --stamp: #d3d3d3;
  }
  html, body {
    margin: 0;
    width: 1200px;
    height: 1200px;
    overflow: hidden;
    background: var(--page);
  }
  .canvas {
    position: relative;
    width: 1200px;
    height: 1200px;
  }
  .postcard {
    position: absolute;
    left: 196px;
    width: 807px;
    height: 523px;
    background: var(--card);
    box-shadow: 0 2px 6px rgba(0,0,0,0.18);
  }
  .postcard--front { top: 57px; }
  .postcard--back { top: 621px; }
  .postcard svg { display: block; width: 100%; height: 100%; }
  .headline { font-family: 'Oswald', sans-serif; font-weight: 500; }
  .detail { font-family: 'Roboto Condensed', sans-serif; }
</style>
</head>
<body>
<main class="canvas">

  <!-- Front side -->
  <section class="postcard postcard--front" aria-label="Postcard front">
    <svg viewBox="0 0 942 610" xmlns="http://www.w3.org/2000/svg">
      <defs>
        <linearGradient id="photoTone" x1="0" y1="0" x2="1" y2="1">
          <stop offset="0" stop-color="#8a8682"/>
          <stop offset="0.45" stop-color="#c9a58a"/>
          <stop offset="0.7" stop-color="#d9653f"/>
          <stop offset="1" stop-color="#b5835c"/>
        </linearGradient>
        <linearGradient id="faintTone" x1="0" y1="0" x2="1" y2="1">
          <stop offset="0" stop-color="#ffffff"/>
          <stop offset="1" stop-color="#f0f0f0"/>
        </linearGradient>
      </defs>

      <rect class="faint-backdrop" x="480" y="0" width="462" height="610" fill="url(#faintTone)" role="img" aria-label="Faint background of scattered credit cards"/>

      <polygon class="photo" points="0,0 454,0 636,610 80,610 0,330" fill="url(#photoTone)" role="img" aria-label="Photo of a stressed woman at a kitchen table reading bills"/>

      <polygon class="contact-band" points="66,532 620,532 643,610 86,610" fill="var(--navy)"/>

      <polygon class="stripe stripe--red" points="454,0 472,0 654,610 636,610" fill="var(--red)"/>
      <polygon class="stripe stripe--grey" points="477,0 491,0 673,610 659,610" fill="var(--grey)"/>
      <polygon class="stripe stripe--red" points="0,326 0,346 72,610 86,610" fill="var(--red)"/>
      <polygon class="corner" points="0,346 0,610 72,610" fill="var(--card)"/>
      <polygon class="stripe stripe--grey" points="0,392 0,410 56,610 68,610" fill="var(--grey)"/>

      <text class="headline" x="897" y="114" text-anchor="end" font-size="60" fill="var(--grey)">YOUR LOGO</text>
      <text class="headline" x="897" y="230" text-anchor="end" font-size="40" fill="var(--ink)">Creditors Calling?</text>
      <text class="headline" x="897" y="278" text-anchor="end" font-size="40" fill="var(--grey)">Mountain of Debt?</text>
      <text class="headline" x="897" y="330" text-anchor="end" font-size="40" fill="var(--ink)">Getting Sued?</text>
      <text class="headline" x="897" y="452" text-anchor="end" font-size="70" font-weight="600" fill="var(--red)">WE CAN</text>
      <text class="headline" x="897" y="536" text-anchor="end" font-size="70" font-weight="600" fill="var(--red)">HELP!</text>

      <g class="contact-line detail" fill="#ffffff">
        <text x="92" y="577" font-size="19">TO KNOW MORE DETAILS</text>
        <g class="icon-phone" transform="translate(316,561)" fill="none" stroke="#ffffff" stroke-width="1.6">
          <path d="M4,2 C2,3 1,6 3,10 C5,14 8,17 12,18 C14,18 16,16 16,15 L13,12 L11,13 C9,12 7,10 6,8 L7,6 Z"/>
        </g>
        <text x="340" y="576" font-size="15">616-392-7158</text>
        <g class="icon-globe" transform="translate(449,570)" fill="none" stroke="#ffffff" stroke-width="1.4">
          <circle r="8.5"/>
          <ellipse rx="3.8" ry="8.5"/>
          <line x1="-8.5" y1="0" x2="8.5" y2="0"/>
          <line x1="-7" y1="-4.5" x2="7" y2="-4.5"/>
          <line x1="-7" y1="4.5" x2="7" y2="4.5"/>
        </g>
        <text x="466" y="576" font-size="14">www.HPDebtRelief.example</text>
      </g>
    </svg>
  </section>

  <!-- Back side -->
  <section class="postcard postcard--back" aria-label="Postcard back">
    <svg viewBox="0 0 942 610" xmlns="http://www.w3.org/2000/svg">
      <defs>
        <linearGradient id="faintToneBack" x1="0" y1="0" x2="1" y2="1">
          <stop offset="0" stop-color="#ffffff"/>
          <stop offset="0.5" stop-color="#f1f1f1"/>
          <stop offset="1" stop-color="#f6f6f6"/>
        </linearGradient>
      </defs>

      <polygon class="faint-backdrop" points="0,120 460,120 356,497 0,497" fill="url(#faintToneBack)" role="img" aria-label="Faint background of scattered credit cards"/>

      <g class="info-section detail" fill="var(--navy)">
        <text x="35" y="51" font-size="13.5">ABOUT BANKRUPTCY PROCESS</text>
        <line x1="213" y1="51" x2="456" y2="51" stroke="var(--grey)" stroke-width="1"/>
        <text x="35" y="267" font-size="13.5">USER TO SUBMIT INFO</text>
        <line x1="170" y1="264" x2="394" y2="264" stroke="var(--grey)" stroke-width="1"/>
      </g>

      <polygon class="stripe stripe--grey" points="483,0 499,0 364,497 348,497" fill="var(--grey)"/>
      <polygon class="stripe stripe--red" points="506,0 523,0 388,497 371,497" fill="var(--red)"/>
      <polygon class="fold-tip" points="378,487 406,497 372,497" fill="#111111"/>

      <polygon class="contact-band" points="0,497 406,497 371,610 0,610" fill="var(--navy)"/>
      <g class="contact-block detail" fill="#ffffff" font-size="13.5">
        <text x="36" y="534">Name: Harbor Pines Debt Relief</text>
        <text x="36" y="552">Phone: 616-392-7158</text>
        <text x="36" y="570">Website: HPDebtRelief.example</text>
      </g>

      <rect class="stamp-box" x="789" y="37" width="108" height="120" fill="var(--stamp)"/>

      <polygon class="stripe stripe--red" points="942,410 942,440 895,610 884,610" fill="var(--red)"/>
      <polygon class="stripe stripe--grey" points="942,462 942,492 914,610 903,610" fill="var(--grey)"/>
    </svg>
  </section>

</main>
</body>
</html>
```